Business Card - Ridge Wellness

Please use the logo / design elements and font to design a business card that is eye catching and informative. If using "Direct Primary Care" logo element, you don't have to spell it out in the text.

Dr. Calvin Pettrow
Ridge Wellness - Direct Primary Care
4817 Tallow Creek Rd. Suite 305
Fort Smith, AR 72903
Phone: 479-555-0173
RidgeWellnessQX.com

```html
<!DOCTYPE html>
<html lang="en">
<head>
<meta charset="utf-8">
<title>Ridge Wellness – Business Card</title>
<link rel="stylesheet" href="https://fonts.googleapis.com/css2?family=Poppins:wght@400;500;600;700&family=Montserrat:wght@400;500&display=swap">
<style>
  :root {
    --bg: #d9d8d6;
    --paper: #ffffff;
    --navy: #0b1538;
    --navy-soft: #1a2a5c;
    --royal: #3a5bb8;
    --cyan: #3fb3e8;
    --ink: #2b2b2b;
    --faint-blue: #e9f4fc;
    --faint-lilac: #e8ebf5;
  }
  * { box-sizing: border-box; margin: 0; padding: 0; }
  html, body { width: 1200px; height: 801px; overflow: hidden; }
  body {
    background: var(--bg);
    display: flex;
    align-items: center;
    justify-content: center;
    gap: 40px;
    font-family: "Montserrat", sans-serif;
  }
  .card {
    position: relative;
    width: 540px;
    height: 309px;
    overflow: hidden;
    border-bottom: 5px solid var(--cyan);
    box-shadow: 0 10px 24px rgba(0,0,0,0.18);
  }
  .card--front { background: var(--paper); }
  .card--back { background: var(--navy); }

  /* front */
  .front-mark {
    position: absolute;
    left: 300px; top: 30px;
    width: 230px; height: 230px;
    border-radius: 50%;
    background: radial-gradient(circle, var(--faint-lilac) 0%, var(--faint-blue) 70%, rgba(233,244,252,0) 100%);
  }
  .accent-square {
    position: absolute;
    right: 0; top: 40px;
    width: 22px; height: 20px;
    background: var(--royal);
  }
  .person {
    position: absolute;
    right: 34px; top: 122px;
    text-align: right;
    white-space: nowrap;
  }
  .person__name {
    font-family: "Poppins", sans-serif;
    font-weight: 700;
    font-size: 19px;
    letter-spacing: 0.4px;
    color: var(--navy);
  }
  .person__role {
    font-size: 12px;
    color: #555;
    margin-top: 1px;
  }
  .brand {
    position: absolute;
    display: flex;
    flex-direction: column;
  }
  .brand__row { display: flex; align-items: center; gap: 8px; white-space: nowrap; }
  .brand__dot { border-radius: 50%; background: var(--royal); flex: none; }
  .brand__name {
    font-family: "Poppins", sans-serif;
    font-weight: 500;
    line-height: 1;
  }
  .brand__tag {
    font-family: "Poppins", sans-serif;
    font-weight: 600;
    letter-spacing: 0.6px;
    display: flex;
    align-items: center;
    gap: 10px;
    white-space: nowrap;
  }
  .brand__tag::before, .brand__tag::after {
    content: "";
    height: 1px;
    flex: 1;
    background: currentColor;
    opacity: 0.8;
  }
  .card--front .brand { left: 30px; top: 42px; width: 236px; }
  .card--front .brand__dot { width: 12px; height: 12px; }
  .card--front .brand__name { font-size: 28px; color: var(--navy); }
  .card--front .brand__tag { font-size: 10px; color: var(--navy); margin-top: 8px; }

  .contact {
    position: absolute;
    left: 34px; top: 168px;
    font-size: 12.5px;
    color: var(--ink);
    line-height: 1.45;
  }
  .contact__address { margin-bottom: 10px; }
  .contact__item { display: flex; align-items: center; gap: 8px; }
  .contact__item svg { width: 11px; height: 11px; flex: none; }
  .contact__web { color: #333; }
  .contact__web strong { color: var(--royal); font-weight: 500; }

  /* back */
  .back-pattern {
    position: absolute; inset: 0;
    background: linear-gradient(135deg, var(--navy) 30%, var(--navy-soft) 100%);
  }
  .card--back .brand {
    left: 50%; top: 50%;
    transform: translate(-50%, -50%);
    width: 360px;
  }
  .card--back .brand__row { justify-content: center; }
  .card--back .brand__dot { width: 18px; height: 18px; }
  .card--back .brand__name { font-size: 42px; color: #fff; }
  .card--back .brand__tag { font-size: 12px; color: #fff; margin-top: 10px; }
</style>
</head>
<body>

  <section class="card card--front">
    <div class="front-mark" role="img" aria-label="Large faint brand symbol in pale blue"></div>
    <div class="accent-square"></div>

    <div class="brand">
      <div class="brand__row">
        <span class="brand__dot"></span>
        <span class="brand__name">Ridge Wellness</span>
      </div>
      <p class="brand__tag">Direct Primary Care</p>
    </div>

    <div class="person">
      <p class="person__name">DR. CALVIN PETTROW</p>
      <p class="person__role">CEO/Founder</p>
    </div>

    <div class="contact">
      <p class="contact__address">4817 Tallow Creek Rd. Suite 305<br>Fort Smith, AR 72903</p>
      <p class="contact__item">
        <svg viewBox="0 0 12 12"><path d="M2.5 1h2l1 2.5-1.3 1a6 6 0 0 0 3.3 3.3l1-1.3 2.5 1v2A1 1 0 0 1 10 10.5 9 9 0 0 1 1.5 2 1 1 0 0 1 2.5 1z" fill="var(--cyan)"/></svg>
        479-555-0173
      </p>
      <p class="contact__item">
        <svg viewBox="0 0 12 12"><rect x="0.5" y="2" width="11" height="8" fill="var(--cyan)"/><path d="M0.5 2l5.5 4.5L11.5 2" fill="none" stroke="#fff" stroke-width="1"/></svg>
        info@RidgeWellnessQX.com
      </p>
      <p class="contact__item contact__web">
        <svg viewBox="0 0 12 12"><circle cx="6" cy="6" r="5.5" fill="var(--cyan)"/><path d="M0.5 6h11M6 0.5c-2.5 3-2.5 8 0 11M6 0.5c2.5 3 2.5 8 0 11" fill="none" stroke="#fff" stroke-width="0.8"/></svg>
        <span>www.<strong>RidgeWellnessQX</strong>.com</span>
      </p>
    </div>
  </section>

  <section class="card card--back">
    <div class="back-pattern" role="img" aria-label="Repeating brand symbol pattern in muted navy tones"></div>
    <div class="brand">
      <div class="brand__row">
        <span class="brand__dot"></span>
        <span class="brand__name">Ridge Wellness</span>
      </div>
      <p class="brand__tag">Direct Primary Care</p>
    </div>
  </section>

</body>
</html>
```